Stationery wanted for Brand New Law Firm

I need a stationery for a law firm that I am establishing. I am after letterhead (black & white and colour version, envelope, document folder, business cards and email signature
The firm will be a "modern" law firm providing commercial advice and transactional assistance to small to medium businesses (sales, purchases and leases of commercial property, business structuring advice, shareholders agreement etc).

Target Market(s)

Small to medium business owners in Sydney, Australia

Industry/Entity Type

Legal

Contact Information for Business Card

Rosalind Penhallow
Principal Lawyer
Penhallow Legal
PO Box 4829 Kellmont Plaza NSW 2187
[Phone No to be provided]
r@penhallowlegal.com.au
www.penhallowlegal.com.au
Tag line - "Expert legal advice for property and business owners"

Colors
ffffff
0555a3
ffc214

Requirements
Must have
• * Attached logo
* Letterhead have colour and black and white options. Other documents to be the same colour scheme as the attached logo.
* Modern, minimalistic feel
* Letterhead and email signature must include the following words:
"Liability limited by a scheme approved under Professional Standards Legislation."

```html
<!DOCTYPE html>
<html lang="en">
<head>
<meta charset="utf-8">
<title>Penhallow Legal — Letterhead</title>
<link rel="stylesheet" href="https://fonts.googleapis.com/css2?family=Libre+Baskerville&family=Questrial&display=swap">
<style>
  :root {
    --paper: #ffffff;
    --backdrop: #ffffff;
    --edge: #8a8a8a;
    --navy: #26234b;
    --gold: #dba84a;
    --ink: #1f1a17;
    --grey: #858585;
  }
  * { margin: 0; padding: 0; box-sizing: border-box; }
  html, body {
    width: 1200px; height: 804px; overflow: hidden;
    background: var(--backdrop);
  }
  .canvas { position: relative; width: 1200px; height: 804px; }
  .letterhead {
    position: absolute; top: 0; width: 569px; height: 804px;
    background: var(--paper);
    border: 1px solid var(--edge);
    --main: var(--navy);
    --accent: var(--gold);
  }
  .letterhead--colour { left: 0; }
  .letterhead--mono { left: 631px; --main: var(--ink); --accent: var(--grey); }

  .brand-name {
    position: absolute; left: 35px; top: 50px;
    font-family: "Libre Baskerville", serif;
    font-size: 24px; letter-spacing: 0.5px;
    color: var(--main);
  }
  .contact {
    position: absolute; left: 421px; top: 49px;
    font-family: "Libre Baskerville", serif;
    font-size: 10.5px; line-height: 13.5px;
    color: var(--main);
  }
  .contact .web { margin-top: 8px; padding-left: 1px; }
  .side-tab {
    position: absolute; left: 554px; top: 37px;
    width: 14px; height: 73px;
    background: var(--accent);
  }
  .legal-note {
    position: absolute; left: 34px; top: 771px;
    font-family: "Questrial", sans-serif;
    font-size: 5.6px; color: var(--main);
  }
  .footer-band {
    position: absolute; left: 0; bottom: 0;
    width: 100%; height: 17px; display: flex;
  }
  .footer-band span { flex: 1; }
  .footer-band .band-main { background: var(--main); }
  .footer-band .band-accent { background: var(--accent); }
</style>
</head>
<body>
<div class="canvas">
  <section class="letterhead letterhead--colour" aria-label="Colour letterhead">
    <div class="brand-name">Penhallow Legal</div>
    <address class="contact" style="font-style:normal">
      <div>address will come here</div>
      <div>address will come here</div>
      <div class="web">www.pnl.com</div>
    </address>
    <div class="side-tab"></div>
    <p class="legal-note">Liability limited by a scheme approved under Professional Standards Legislation.”</p>
    <div class="footer-band"><span class="band-main"></span><span class="band-accent"></span></div>
  </section>

  <section class="letterhead letterhead--mono" aria-label="Black and white letterhead">
    <div class="brand-name">Penhallow Legal</div>
    <address class="contact" style="font-style:normal">
      <div>address will come here</div>
      <div>address will come here</div>
      <div class="web">www.pnl.com</div>
    </address>
    <div class="side-tab"></div>
    <p class="legal-note">Liability limited by a scheme approved under Professional Standards Legislation.”</p>
    <div class="footer-band"><span class="band-main"></span><span class="band-accent"></span></div>
  </section>
</div>
</body>
</html>
```